Business card design needed

We are 2 artists starting up a studio by the water in Sydney ...where we can work and display our art...would like the back ground to be Navy and white stripe...nautical...and the name The Paint Hut to be bold and the main wording...not nautical...if possible thought the A for art could be an easel ...ie the capital A using the cross bar as the platform that paint would be circles of colour....would like the main wording in Black but the easel A in colour
Hope u are able to help
thanku Lorna Vesk
as I will be away in a week for 4 weeks could u please send all info to Mira Colbins email....she can contact me and we can go ahead asap....

Artists

THE PAINT HUT

Hallorans Oar House
The Reach..17 Kellaby Rd..Dunrook 2091 Sydney

Mir Colbin..0437819025..miracolbin@mailnest.example
Lorn Vesk...0429573816..lvesk@harborlink.example

```html
<!DOCTYPE html>
<html lang="en">
<head>
<meta charset="utf-8">
<title>The Paint Hut – Business Card</title>
<link rel="stylesheet" href="https://fonts.googleapis.com/css2?family=Encode+Sans+Semi+Condensed:wght@400;600&display=swap">
<style>
  :root {
    --navy: #00304f;
    --white: #ffffff;
    --ink: #111111;
    --text: #1a1a1a;
    --rope: #2b2b2b;
  }
  * { box-sizing: border-box; margin: 0; padding: 0; }
  html, body {
    width: 1200px;
    height: 684px;
    overflow: hidden;
    background: var(--white);
  }
  .card {
    position: relative;
    width: 1200px;
    height: 684px;
    background: var(--white);
    font-family: "Encode Sans Semi Condensed", "Arial Narrow", sans-serif;
    color: var(--text);
  }
  .stripes {
    position: absolute;
    left: 0;
    top: 0;
  }
  .emblem {
    position: absolute;
    left: 374px;
    top: 43px;
    width: 456px;
    height: 456px;
  }
  .brand-name {
    position: absolute;
    left: 374px;
    top: 43px;
    width: 456px;
    height: 456px;
    display: flex;
    align-items: center;
    justify-content: center;
    text-align: center;
    font-size: 66px;
    font-weight: 600;
    line-height: 1.05;
    color: var(--ink);
  }
  .contacts {
    position: absolute;
    top: 574px;
    left: 0;
    width: 1200px;
    font-size: 24px;
    line-height: 36px;
    letter-spacing: 0.2px;
  }
  .address {
    position: absolute;
    right: 706px;
    text-align: right;
    white-space: nowrap;
  }
  .people {
    position: absolute;
    left: 541px;
    text-align: left;
    white-space: nowrap;
  }
</style>
</head>
<body>
  <main class="card">
    <svg class="stripes" width="1200" height="520" viewBox="0 0 1200 520" aria-hidden="true">
      <rect x="0" y="32" width="1200" height="67" fill="var(--navy)"/>
      <rect x="0" y="168" width="1200" height="68" fill="var(--navy)"/>
      <rect x="0" y="305" width="1200" height="68" fill="var(--navy)"/>
      <rect x="0" y="444" width="1200" height="69" fill="var(--navy)"/>
    </svg>

    <svg class="emblem" viewBox="0 0 456 456">
      <circle cx="228" cy="228" r="228" fill="var(--white)"/>
      <circle cx="228" cy="228" r="212" fill="none" stroke="var(--rope)" stroke-width="22"
              role="img" aria-label="Twisted rope frame around the emblem"/>
      <circle cx="228" cy="228" r="198" fill="var(--white)"/>
    </svg>

    <h1 class="brand-name">The Paint<br>Hut</h1>

    <section class="contacts">
      <p class="address">Hallorans Oar House, The Reach.<br>17 Kellaby Rd, Dunrook 2091 Sydney</p>
      <p class="people">Mir Colbin: 0437819025, miracolbin@mailnest.example<br>Lorn Vesk: 0429573816, lvesk@harborlink.example</p>
    </section>
  </main>
</body>
</html>
```